NEW YORK Plumbing/utility company 10 year anniversary business card

Looking For simple back and front business card would like to include a few things in description
We offer 24/7 emergency service
residential
commercial
industrial
municipal
services offered
Plumbing
hydro excavation
hydro jetting
Well pumps
Sewer pumps
water mains
sewer mains

```html
<!DOCTYPE html>
<html lang="en">
<head>
<meta charset="utf-8">
<title>KRW Business Card — Front and Back</title>
<link href="https://fonts.googleapis.com/css2?family=Roboto+Condensed:wght@400;700;800&family=Montserrat:wght@600&display=swap" rel="stylesheet">
<style>
  :root {
    --backdrop: #d9d9d9;
    --card: #ffffff;
    --brand-blue: #166cd9;
    --aqua: #4dd3f5;
    --slate: #7b8b8a;
    --alert-red: #ee1a1a;
    --mist: #e4e4e4;
    --rule: #9aa5a5;
  }
  * { box-sizing: border-box; margin: 0; padding: 0; }
  html, body {
    width: 1200px; height: 846px; overflow: hidden;
    background: var(--backdrop);
    font-family: "Roboto Condensed", Arial, sans-serif;
  }
  .card {
    position: absolute; left: 346px; width: 508px; height: 290px;
    background: var(--card); overflow: hidden;
  }
  .card--front { top: 99px; }
  .card--back { top: 456px; }

  /* Front */
  .brand-name {
    position: absolute; left: 0; right: 0; top: 40px;
    text-align: center; font-weight: 800; font-size: 96px; line-height: 1;
    color: var(--brand-blue); letter-spacing: 4px;
  }
  .contact-row {
    position: absolute; left: 0; right: 0; top: 164px;
    display: flex; justify-content: center; align-items: center; gap: 8px;
    color: var(--slate); font-weight: 700; font-size: 23px;
  }
  .contact-item { display: flex; align-items: center; gap: 6px; }
  .contact-icon { width: 22px; height: 22px; }
  .divider {
    position: absolute; left: 86px; width: 332px; top: 202px;
    height: 1px; background: var(--rule);
  }
  .emergency {
    position: absolute; left: 0; right: 0; top: 215px;
    text-align: center; color: var(--alert-red);
    font-weight: 800; font-size: 18px; letter-spacing: .2px;
  }
  .sectors {
    position: absolute; left: 0; right: 0; top: 242px;
    display: flex; justify-content: center; gap: 12px;
    list-style: none; color: var(--slate); font-weight: 700; font-size: 16px;
  }
  .sectors li { display: flex; align-items: center; gap: 8px; }
  .dot { width: 10px; height: 10px; border-radius: 50%; flex: none; }
  .dot--red { background: var(--alert-red); }
  .dot--aqua { background: var(--aqua); }

  /* Back */
  .anniversary {
    position: absolute; left: 60px; top: 30px; width: 140px;
    text-align: center; color: var(--brand-blue);
  }
  .anniversary-number { font-weight: 800; font-size: 92px; line-height: .95; }
  .anniversary-label {
    font-family: "Montserrat", Arial, sans-serif; font-weight: 600;
    color: var(--slate); font-size: 13px; letter-spacing: 2px;
  }
  .brand-name--small {
    top: 150px; left: 33px; right: auto; width: 192px;
    font-size: 60px; letter-spacing: 3px;
  }
  .company-line {
    position: absolute; left: 33px; width: 192px; top: 225px;
    text-align: center; font-family: "Montserrat", Arial, sans-serif;
    font-weight: 600; color: var(--brand-blue);
  }
  .company-line .region { font-size: 17px; letter-spacing: 2px; display: block; }
  .company-line .trade { font-size: 13px; letter-spacing: 2px; display: block; margin-top: 6px; }
  .services-panel {
    position: absolute; left: 252px; top: -40px; width: 300px; height: 380px;
    background: var(--mist); border-radius: 50% 50% 48% 48% / 55% 55% 45% 45%;
  }
  .services-title {
    position: absolute; left: 344px; top: 28px;
    color: var(--aqua); font-weight: 800; font-size: 20px; line-height: 1.05;
  }
  .services-list {
    position: absolute; left: 332px; top: 74px; list-style: none;
    color: var(--slate); font-weight: 700; font-size: 16px;
  }
  .services-list li { display: flex; align-items: center; gap: 6px; height: 28.3px; }
</style>
</head>
<body>
  <section class="card card--front" aria-label="Card front">
    <div class="brand-name">KRW</div>
    <div class="contact-row">
      <span class="contact-item">
        <svg class="contact-icon" viewBox="0 0 22 22" aria-hidden="true">
          <circle cx="11" cy="11" r="11" fill="var(--brand-blue)"/>
          <path d="M7.5 5.5c.6-.4 1.3 0 1.6.6l.9 1.8c.2.5 0 1-.4 1.3l-.8.5c.6 1.6 1.6 2.7 3.1 3.4l.6-.8c.3-.4.9-.5 1.3-.3l1.8 1c.6.3.8 1 .4 1.6l-.7.9c-.7.8-2 .9-3.2.3-2.6-1.3-4.5-3.4-5.5-6.1-.4-1.2-.1-2.3.9-2.9z" fill="#fff"/>
        </svg>
        555 014 2286
      </span>
      <span class="contact-item">
        <svg class="contact-icon" viewBox="0 0 22 22" aria-hidden="true">
          <circle cx="11" cy="11" r="11" fill="var(--brand-blue)"/>
          <rect x="5" y="7" width="12" height="8.5" rx="1" fill="none" stroke="#fff" stroke-width="1.4"/>
          <path d="M5.4 7.6 11 12l5.6-4.4M5.4 15 9.3 10.8M16.6 15l-3.9-4.2" fill="none" stroke="#fff" stroke-width="1.2"/>
        </svg>
        info@KRWNY.com
      </span>
    </div>
    <div class="divider"></div>
    <p class="emergency">WE OFFER 24/7 EMERGENCY SERVICE</p>
    <ul class="sectors">
      <li><span class="dot dot--red"></span>residential</li>
      <li><span class="dot dot--red"></span>commercial</li>
      <li><span class="dot dot--red"></span>industrial</li>
      <li><span class="dot dot--red"></span>municipal</li>
    </ul>
  </section>

  <section class="card card--back" aria-label="Card back">
    <div class="anniversary">
      <div class="anniversary-number">10</div>
      <div class="anniversary-label">YEARS ANNIVERSARY</div>
    </div>
    <div class="brand-name brand-name--small">KRW</div>
    <div class="company-line">
      <span class="region">MILL CREEK</span>
      <span class="trade">WATER &amp; SEWER</span>
    </div>
    <div class="services-panel" aria-hidden="true"></div>
    <h2 class="services-title">SERVICES<br>OFFERED</h2>
    <ul class="services-list">
      <li><span class="dot dot--aqua"></span>Plumbing</li>
      <li><span class="dot dot--aqua"></span>Hydro excavation</li>
      <li><span class="dot dot--aqua"></span>Hydro jetting</li>
      <li><span class="dot dot--aqua"></span>Well pumps</li>
      <li><span class="dot dot--aqua"></span>Sewer pumps</li>
      <li><span class="dot dot--aqua"></span>Sewer mains</li>
      <li><span class="dot dot--aqua"></span>Water mains</li>
    </ul>
  </section>
</body>
</html>
```